R&t Subterra

We specialize in CIPP pipe lining but do other underground utilities trenchless as well.

Target Market(s)

Trenchless sewer replacement

Contact Information for Business Card

Gavin Holtby 715-482-6130 Pinecrest Falls, wi

```html
<!DOCTYPE html>
<html lang="en">
<head>
<meta charset="utf-8">
<title>R&amp;t Subterra – Business Card</title>
<link href="https://fonts.googleapis.com/css2?family=Montserrat:wght@400;500;700;800&display=swap" rel="stylesheet">
<style>
  :root {
    --backdrop: #cdcdcd;
    --card: #ffffff;
    --brand-blue: #2e8bcb;
    --ink: #1c1c1c;
    --shadow: rgba(0, 0, 0, 0.28);
  }
  * { margin: 0; padding: 0; box-sizing: border-box; }
  html, body {
    width: 1200px;
    height: 800px;
    overflow: hidden;
    background: var(--backdrop);
    font-family: "Montserrat", sans-serif;
  }
  .canvas { position: relative; width: 1200px; height: 800px; }

  .card {
    position: absolute;
    left: 422px;
    width: 422px;
    height: 240px;
    background: var(--card);
    border-radius: 12px;
    box-shadow: 2px 3px 4px var(--shadow);
  }
  .card--front { top: 130px; }
  .card--back { top: 430px; }

  .brand {
    position: absolute;
    display: flex;
    align-items: center;
    color: var(--brand-blue);
    font-weight: 800;
    white-space: nowrap;
  }
  .brand__dot { flex: none; border-radius: 50%; background: var(--brand-blue); }
  .card--front .brand { left: 30px; top: 107px; font-size: 17px; gap: 8px; }
  .card--front .brand__dot { width: 24px; height: 24px; }
  .card--back .brand { left: 42px; top: 96px; font-size: 37px; gap: 14px; }
  .card--back .brand__dot { width: 46px; height: 46px; }

  .divider {
    position: absolute;
    left: 223px;
    top: 65px;
    width: 1.5px;
    height: 109px;
    background: var(--brand-blue);
  }
  .details { position: absolute; left: 244px; top: 60px; color: var(--ink); white-space: nowrap; }
  .details__name { font-size: 17px; font-weight: 700; color: var(--brand-blue); line-height: 1.2; }
  .details__role { font-size: 12px; font-weight: 500; margin-top: 1px; }
  .contact { list-style: none; font-size: 12.2px; }
  .contact--place { margin-top: 11px; }
  .contact--reach { margin-top: 9px; }
  .contact__item { display: flex; align-items: center; gap: 4px; line-height: 15px; }
  .contact__icon { width: 9px; height: 10px; flex: none; fill: var(--brand-blue); }
</style>
</head>
<body>
<main class="canvas">
  <section class="card card--front" aria-label="Business card front">
    <div class="brand">
      <span class="brand__dot"></span>
      <span class="brand__name">R&amp;t Subterra</span>
    </div>
    <div class="divider"></div>
    <div class="details">
      <p class="details__name">Gavin Holtby</p>
      <p class="details__role">Managing Director</p>
      <ul class="contact contact--place">
        <li class="contact__item">
          <svg class="contact__icon" viewBox="0 0 10 12"><path d="M5 0a4 4 0 0 0-4 4c0 3 4 8 4 8s4-5 4-8a4 4 0 0 0-4-4zm0 5.6A1.6 1.6 0 1 1 5 2.4a1.6 1.6 0 0 1 0 3.2z"/></svg>
          Pinecrest Falls, wi
        </li>
      </ul>
      <ul class="contact contact--reach">
        <li class="contact__item">
          <svg class="contact__icon" viewBox="0 0 10 10"><path d="M1 3c0-1 1.5-1.8 4-1.8S9 2 9 3v1H7V3H3v1H1zM2 5h6l1 4H1z"/></svg>
          715-482-6130
        </li>
        <li class="contact__item">
          <svg class="contact__icon" viewBox="0 0 10 10"><path d="M0 2h10v6H0zm1 1v.4l4 2.6 4-2.6V3z"/></svg>
          info@rtsubterra.com
        </li>
        <li class="contact__item">
          <svg class="contact__icon" viewBox="0 0 10 10"><circle cx="5" cy="5" r="4.5"/><path d="M2.5 3.5l2 .5v2l-1 1.5M6 2l1.5 1.5L6.5 6" stroke="#fff" stroke-width="0.8" fill="none"/></svg>
          www.rtsubterra.com
        </li>
      </ul>
    </div>
  </section>

  <section class="card card--back" aria-label="Business card back">
    <div class="brand">
      <span class="brand__dot"></span>
      <span class="brand__name">R&amp;t Subterra</span>
    </div>
  </section>
</main>
</body>
</html>
```